HUSH: Halt Usual Stuff Happily school library event

I need two poster designs for Halt Usual Stuff Happily (HUSH) in BC, requested by the CSMKA--Cedarvale School Media Keepers' Association. One should be for elementary students and one for high school. I want the date (Monday, October 26, 2020) and Halt Usual Stuff Happily. I would like the posters in English and in French. French is : Mets Ta Journée En Pause! I'm including last year's posters as examples. I would like to be able to print the poster files on 11x17 paper.

Requirements
Must have
• -The phrase "Halt Usual Stuff Happily" for the English version; "Mets Ta Journée En Pause" for the French version.
-Include the organization name: Cedarvale School Media Keepers' Association
-The date: Monday, October 26, 2020
Nice to have
• I would like the elementary version to be bright and colourful--fun for younger kids. I would like the high school version to be a bit more mature for the older students. Can still be bright and colourful.

```html
<!DOCTYPE html>
<html lang="fr">
<head>
<meta charset="utf-8">
<title>Mets Ta Journée En Pause</title>
<link rel="stylesheet" href="https://fonts.googleapis.com/css2?family=Archivo+Black&family=Montserrat:wght@500;700&display=swap">
<style>
  :root {
    --magenta: #b8155a;
    --magenta-deep: #7a0c3a;
    --shadow: #2a0614;
    --yellow: #dcc01e;
    --white: #ffffff;
  }
  * { margin: 0; padding: 0; box-sizing: border-box; }
  html, body {
    width: 800px;
    height: 1200px;
    overflow: hidden;
    background: var(--shadow);
  }
  .poster {
    position: relative;
    width: 800px;
    height: 1200px;
    overflow: hidden;
  }
  .poster__photo {
    position: absolute;
    inset: 0;
    background:
      radial-gradient(ellipse 70% 60% at 48% 55%, var(--magenta) 0%, var(--magenta) 45%, var(--magenta-deep) 75%, var(--shadow) 100%);
  }
  .title {
    position: absolute;
    inset: 0;
    font-family: "Archivo Black", "Arial Black", sans-serif;
    color: var(--yellow);
    text-transform: uppercase;
    text-align: center;
  }
  .title__line {
    position: absolute;
    left: 0;
    right: 0;
    font-size: 168px;
    line-height: 1;
    letter-spacing: -3px;
  }
  .title__line--1 { top: 12px; }
  .title__line--2 { top: 207px; }
  .title__line--3 { top: 412px; font-size: 124px; letter-spacing: -2px; }
  .title__line--4 { top: 597px; }
  .title__line--5 { top: 792px; }
  .credit {
    position: absolute;
    left: 0;
    right: 0;
    text-align: center;
    font-family: "Montserrat", Arial, sans-serif;
    color: var(--white);
  }
  .credit__label {
    top: 989px;
    font-size: 15px;
    font-weight: 500;
    letter-spacing: 0.3em;
  }
  .credit__org {
    top: 1032px;
    font-size: 19px;
    font-weight: 700;
    line-height: 27px;
    letter-spacing: 0.02em;
    text-transform: uppercase;
  }
  .event-date {
    position: absolute;
    left: 0;
    right: 0;
    top: 1118px;
    text-align: center;
    font-family: "Archivo Black", "Arial Black", sans-serif;
    font-size: 40px;
    line-height: 1;
    letter-spacing: -1px;
    color: var(--yellow);
  }
</style>
</head>
<body>
  <main class="poster">
    <div class="poster__photo" role="img" aria-label="Photo en duotone magenta d'une pile de livres empilés, certains ouverts"></div>

    <h1 class="title">
      <span class="title__line title__line--1">Mets</span>
      <span class="title__line title__line--2">Ta</span>
      <span class="title__line title__line--3">Journée</span>
      <span class="title__line title__line--4">En</span>
      <span class="title__line title__line--5">Pause</span>
    </h1>

    <p class="credit credit__label">PRÉSENTÉ PAR</p>
    <p class="credit credit__org">Cedarvale School Media<br>Keepers’ Association</p>

    <p class="event-date">LUN // OCTOBRE 26 // 2020</p>
  </main>
</body>
</html>
```